Business Card Design

New business card design

Target Market(s)

Residential & Commercial Property Managers

Industry/Entity Type

Plumbing Services

Contact Information for Business Card

Name - Tom Brereton, title - Director, Phone Number - 0431 862 517, email - tom@rvk-plumbing.com.au, Company ABN - 73 512 938 204,

Font styles to use
Sans Serif

Colors
0054AA
0677BA
7BADD7
CADEEF
E8F1F8

```html
<!DOCTYPE html>
<html lang="en">
<head>
<meta charset="utf-8">
<title>RVK Plumbing Services – Business Card</title>
<link rel="stylesheet" href="https://fonts.googleapis.com/css2?family=Arimo:wght@400;700&display=swap">
<style>
  :root {
    --page-bg: #e4e5e6;
    --card-dark: #1d2227;
    --card-light: #f3f4f5;
    --accent-blue: #0d9fe0;
    --text-light: #ffffff;
    --text-dark: #1d2227;
  }
  * { box-sizing: border-box; margin: 0; padding: 0; }
  html, body {
    width: 1200px; height: 1040px; overflow: hidden;
    background: var(--page-bg);
    font-family: "Arimo", Arial, sans-serif;
  }
  .card {
    position: absolute;
    left: 284px;
    width: 640px; height: 365px;
    border-radius: 18px;
    overflow: hidden;
    background: var(--card-dark);
    box-shadow: 0 3px 6px rgba(0,0,0,0.25);
  }
  .card--front { top: 130px; }
  .card--back { top: 568px; }

  .front-panel { position: absolute; inset: 0; }

  .contact-name {
    position: absolute; left: 46px; top: 34px;
    font-size: 27px; font-weight: 700; color: var(--accent-blue);
    letter-spacing: 0.2px;
  }
  .contact-title {
    position: absolute; left: 47px; top: 68px;
    font-size: 15px; font-weight: 400; color: var(--text-light);
  }
  .contact-abn {
    position: absolute; left: 47px; top: 250px;
    font-size: 15.5px; color: var(--text-light);
  }
  .contact-list {
    position: absolute; left: 47px; top: 284px;
    list-style: none;
  }
  .contact-list li {
    display: flex; align-items: center; gap: 9px;
    font-size: 15.5px; color: var(--text-light);
    height: 19px;
  }
  .contact-list svg { width: 13px; height: 13px; fill: var(--accent-blue); }

  .brand-name {
    position: absolute;
    font-weight: 400;
    white-space: nowrap;
    text-align: center;
    line-height: 1;
  }
  .brand-name--front {
    left: 290px; width: 340px; top: 160px;
    font-size: 28px; color: var(--text-dark);
  }
  .brand-name--back {
    left: 0; right: 0; top: 160px;
    font-size: 44px; color: var(--text-light);
  }
</style>
</head>
<body>

<section class="card card--front" aria-label="Business card front">
  <svg class="front-panel" viewBox="0 0 640 365" width="640" height="365" aria-hidden="true">
    <path d="M436 0 L247 166 Q230 184 247 205 L410 365 L640 365 L640 0 Z" fill="var(--card-light)"/>
    <path d="M428 0 L239 166 Q222 184 239 205 L402 365" fill="none" stroke="var(--accent-blue)" stroke-width="6"/>
  </svg>

  <h1 class="contact-name">Tom Brereton</h1>
  <p class="contact-title">Director</p>
  <p class="contact-abn">ABN - 73 512 938 204</p>
  <ul class="contact-list">
    <li>
      <svg viewBox="0 0 24 24"><path d="M6.6 10.8a15.1 15.1 0 0 0 6.6 6.6l2.2-2.2a1 1 0 0 1 1-.25 11.4 11.4 0 0 0 3.6.57 1 1 0 0 1 1 1V20a1 1 0 0 1-1 1A17 17 0 0 1 3 4a1 1 0 0 1 1-1h3.5a1 1 0 0 1 1 1c0 1.25.2 2.45.57 3.6a1 1 0 0 1-.25 1z"/></svg>
      0431 862 517
    </li>
    <li>
      <svg viewBox="0 0 24 24"><path d="M2 5h20v14H2z M3.5 6.5 12 13l8.5-6.5" fill="var(--accent-blue)" stroke="var(--card-dark)" stroke-width="1.5"/></svg>
      tom@rvk-plumbing.com.au
    </li>
  </ul>

  <p class="brand-name brand-name--front">RVK Plumbing Services</p>
</section>

<section class="card card--back" aria-label="Business card back">
  <p class="brand-name brand-name--back">RVK Plumbing Services</p>
</section>

</body>
</html>
```